Lantern Keepers Lantern Scribes

We would like the business card to be Horizontal
Logo on the back and want it raised.

Target Market(s)

Education and Museums

Industry/Entity Type

Education

Contact Information for Business Card

Joanne Valdoro, P.H.D.
2918 Pemberly Rd
Laurel, MD 20914
612.447.3091
Joanne.Valdoro@lanternkeeperslanternscribes.org
lanternkeeperslanternscribes.org

Font styles to use
Serif

Colors

Designer to choose colors to be used in the design.

Requirements
Must have
• letters and logo must be raised
• Must be slate blue card
• Silver is aluminum foil

```html
<!DOCTYPE html>
<html lang="en">
<head>
<meta charset="utf-8">
<title>Lantern Keepers Lantern Scribes — Business Card</title>
<link rel="stylesheet" href="https://fonts.googleapis.com/css2?family=Lora:wght@400;700&display=swap">
<style>
  :root {
    --backdrop: #2c2d30;
    --card: #2e3c54;
    --card-deep: #25314a;
    --foil-light: #f2f3f5;
    --foil-mid: #b3b6bc;
    --foil-dark: #6b6e74;
    --ink-name: #c9ccd2;
    --ink-detail: #e1e3e7;
    --ink-muted: #aeb3bc;
    --rule: #8c93a0;
  }
  * { box-sizing: border-box; margin: 0; padding: 0; }
  html, body { width: 1200px; height: 900px; overflow: hidden; }
  body {
    background: radial-gradient(ellipse at 50% 45%, #36373a 0%, var(--backdrop) 60%, #232427 100%);
    font-family: "Lora", Georgia, serif;
    position: relative;
  }
  .card {
    position: absolute;
    width: 600px;
    height: 350px;
    background: linear-gradient(160deg, var(--card) 0%, var(--card-deep) 100%);
    box-shadow: 0 18px 30px rgba(0,0,0,0.45);
    overflow: hidden;
  }
  .card::after {
    content: "";
    position: absolute;
    left: 0; right: 0; bottom: 0;
    height: 7px;
    background: linear-gradient(90deg, var(--foil-dark) 0%, var(--foil-light) 30%, var(--foil-mid) 55%, var(--foil-light) 78%, var(--foil-dark) 100%);
  }
  .card--front { left: 480px; top: 60px; }
  .card--back { left: 140px; top: 470px; }

  .brand {
    position: absolute;
    inset: 0 0 7px 0;
    display: flex;
    align-items: center;
    justify-content: center;
    gap: 16px;
  }
  .brand__dot {
    width: 26px; height: 26px;
    border-radius: 50%;
    border: 2px solid var(--foil-light);
    flex: none;
  }
  .brand__name {
    color: var(--foil-light);
    font-weight: 700;
    font-size: 19px;
    letter-spacing: 1px;
    text-transform: uppercase;
    width: 240px;
    line-height: 1.3;
  }

  .holder {
    position: absolute;
    left: 36px; top: 132px;
    color: var(--ink-name);
    font-weight: 700;
    font-size: 18px;
    letter-spacing: 0.5px;
    white-space: nowrap;
  }
  .divider {
    position: absolute;
    left: 228px; top: 112px;
    width: 1px; height: 68px;
    background: var(--rule);
  }
  .contact {
    position: absolute;
    left: 242px; top: 118px;
    list-style: none;
    color: var(--ink-detail);
    font-size: 11.5px;
    line-height: 20px;
    white-space: nowrap;
  }
  .contact li { display: flex; align-items: center; gap: 7px; }
  .contact svg { width: 11px; height: 11px; fill: var(--ink-detail); flex: none; }
  .address {
    position: absolute;
    left: 36px; top: 236px;
    color: var(--ink-muted);
    font-size: 14px;
  }
</style>
</head>
<body>
  <section class="card card--front" aria-label="Card front">
    <div class="brand">
      <span class="brand__dot"></span>
      <span class="brand__name">Lantern Keepers Lantern Scribes</span>
    </div>
  </section>

  <section class="card card--back" aria-label="Card back">
    <h1 class="holder">JOANNE VALDORO</h1>
    <span class="divider"></span>
    <ul class="contact">
      <li>
        <svg viewBox="0 0 12 12" aria-hidden="true"><path d="M1 3.5 C1 2 2 1.5 3 1.5 H9 C10 1.5 11 2 11 3.5 L9 4.5 L8 3 H4 L3 4.5 Z M3 5.5 H9 L10 10.5 H2 Z"/></svg>
        <span>612.447.3091</span>
      </li>
      <li>
        <svg viewBox="0 0 12 12" aria-hidden="true"><path d="M1 2.5 H11 V9.5 H1 Z M1.8 3.3 L6 6.6 L10.2 3.3 V3.2 H1.8 Z" fill-rule="evenodd"/></svg>
        <span>Joanne.Valdoro@lanternkeeperslanternscribes.org</span>
      </li>
      <li>
        <svg viewBox="0 0 12 12" aria-hidden="true"><circle cx="6" cy="6" r="5"/></svg>
        <span>lanternkeeperslanternscribes.org</span>
      </li>
    </ul>
    <p class="address">2918 Pemberly Rd, Laurel, MD 20914</p>
  </section>
</body>
</html>
```